MORVA Design

We have a 5 part framework that companies use to plot their social media strategies and digital transformation activity. We would like to display the 5 elements in a circular format (please see the attachment for our current design - we want to get a better version of that).

The five elements and their meaning can be read about here: http://quellagrove.example/morva/what-is-morva/
We would like to see designs that fit our corporate image but also maintain informality and simplicity…. Ive included another image of some of the icons we've been using and enjoying to give an understanding of the stuff we like

Target Market(s)

Corporates

Industry/Entity Type

Digital

Logo Text

Brokerage, Integration, Trust, Incentives, Leadership

Colors
0255a3

Requirements
Must have
• Must be circular in format with each element neatly labelled - PLEASE REVIEW OUR CURRENT VERSION IN THE ATTACHMENTS

```html
<!DOCTYPE html>
<html lang="en">
<head>
<meta charset="utf-8">
<title>Five-Part Framework</title>
<link href="https://fonts.googleapis.com/css2?family=Lato:wght@400&display=swap" rel="stylesheet">
<style>
  :root {
    --brand-teal: #00999a;
    --brand-teal-soft: #bfe5e5;
    --canvas-bg: #ffffff;
  }
  html, body {
    margin: 0;
    padding: 0;
    width: 1200px;
    height: 1000px;
    overflow: hidden;
    background: var(--canvas-bg);
  }
  .framework {
    display: block;
    width: 1200px;
    height: 1000px;
  }
  .framework__ring {
    fill: none;
    stroke: var(--brand-teal);
    stroke-width: 8;
  }
  .element__disc {
    fill: var(--canvas-bg);
    stroke: var(--brand-teal);
    stroke-width: 7;
  }
  .element__label {
    font-family: "Lato", "Gill Sans", sans-serif;
    font-size: 14px;
    letter-spacing: 1.2px;
    fill: var(--brand-teal);
    text-transform: uppercase;
  }
  .icon-line {
    fill: none;
    stroke: var(--brand-teal);
    stroke-width: 3;
    stroke-linecap: round;
    stroke-linejoin: round;
  }
  .icon-solid {
    fill: var(--brand-teal);
  }
  .icon-coin {
    fill: var(--brand-teal);
    stroke: var(--canvas-bg);
    stroke-width: 2;
  }
  .icon-placeholder {
    fill: url(#softTeal);
  }
</style>
</head>
<body>
<svg class="framework" viewBox="0 0 1200 1000" xmlns="http://www.w3.org/2000/svg" aria-label="Five-part framework: Brokerage, Leadership, Incentives, Trust, Integration">
  <defs>
    <radialGradient id="softTeal">
      <stop offset="0%" stop-color="#7fcccc"/>
      <stop offset="100%" stop-color="#bfe5e5"/>
    </radialGradient>
    <path id="arc-brokerage" d="M512,387.2 A68,68 0 0 1 646,387.2"/>
    <path id="arc-leadership" d="M705.8,411 A68,68 0 0 1 705.8,545"/>
    <path id="arc-integration" d="M445.2,543 A68,68 0 0 1 445.2,409"/>
    <path id="arc-trust" d="M442.7,558.6 A80,80 0 0 0 544,679.3"/>
    <path id="arc-incentives" d="M588.7,659.4 A80,80 0 0 0 725.2,580.6"/>
  </defs>

  <circle class="framework__ring" cx="578" cy="520" r="135"/>

  <g class="element element--brokerage">
    <circle class="element__disc" cx="579" cy="399" r="58"/>
    <g class="icon-line">
      <circle cx="545" cy="387" r="7"/>
      <path d="M535,412 v-8 q0,-6 6,-8 h8 q6,2 6,8 v8 z"/>
      <circle cx="613" cy="387" r="7"/>
      <path d="M603,412 v-8 q0,-6 6,-8 h8 q6,2 6,8 v8 z"/>
      <path d="M562,393 h34 M567,388 l-5,5 l5,5 M591,388 l5,5 l-5,5"/>
    </g>
    <text class="element__label"><textPath href="#arc-brokerage" startOffset="50%" text-anchor="middle">Brokerage</textPath></text>
  </g>

  <g class="element element--leadership">
    <circle class="element__disc" cx="694" cy="478" r="58"/>
    <circle class="icon-placeholder" cx="694" cy="478" r="38" role="img" aria-label="Whistle on a lanyard icon"/>
    <text class="element__label"><textPath href="#arc-leadership" startOffset="50%" text-anchor="middle">Leadership</textPath></text>
  </g>

  <g class="element element--incentives">
    <circle class="element__disc" cx="650" cy="608" r="58"/>
    <g class="coin-stack">
      <ellipse class="icon-coin" cx="648" cy="634" rx="21" ry="5"/>
      <ellipse class="icon-coin" cx="648" cy="626" rx="21" ry="5"/>
      <ellipse class="icon-coin" cx="648" cy="618" rx="21" ry="5"/>
      <ellipse class="icon-coin" cx="648" cy="610" rx="21" ry="5"/>
      <ellipse class="icon-coin" cx="648" cy="602" rx="21" ry="5"/>
      <ellipse class="icon-coin" cx="648" cy="593" rx="21" ry="6"/>
    </g>
    <text class="element__label"><textPath href="#arc-incentives" startOffset="50%" text-anchor="middle">Incentives</textPath></text>
  </g>

  <g class="element element--trust">
    <circle class="element__disc" cx="504" cy="610" r="58"/>
    <circle class="icon-placeholder" cx="504" cy="610" r="38" role="img" aria-label="Handshake icon"/>
    <text class="element__label"><textPath href="#arc-trust" startOffset="50%" text-anchor="middle">Trust</textPath></text>
  </g>

  <g class="element element--integration">
    <circle class="element__disc" cx="457" cy="476" r="58"/>
    <g class="icon-solid">
      <rect x="424" y="461" width="28" height="28"/>
      <circle cx="438" cy="460" r="5"/>
      <circle cx="438" cy="490" r="5"/>
      <circle cx="423" cy="475" r="4" fill="#ffffff"/>
      <rect x="455" y="461" width="28" height="28"/>
      <circle cx="469" cy="460" r="5"/>
      <circle cx="469" cy="490" r="5"/>
      <circle cx="484" cy="475" r="5"/>
      <circle cx="455" cy="475" r="4" fill="#ffffff"/>
    </g>
    <text class="element__label"><textPath href="#arc-integration" startOffset="50%" text-anchor="middle">Integration</textPath></text>
  </g>
</svg>
</body>
</html>
```